Business Card Project

We are a small consulting firm. You can experiment with any design.
Must have:
1) Company name - TOLVIN International
2) Company slogan - simple solutions for complex problems
3) Name/Title/Phone/Email/WWW/ - use anything you like as an example.

Industry/Entity Type

Business

```html
<!DOCTYPE html>
<html lang="en">
<head>
<meta charset="utf-8">
<title>TOLVIN International – Business Card</title>
<link href="https://fonts.googleapis.com/css2?family=Exo+2:wght@400;500&display=swap" rel="stylesheet">
<style>
  :root {
    --bg: #ecebe8;
    --card-white: #ffffff;
    --brand-blue: #29a8e0;
    --ink: #222222;
    --logo-grey: #5c5c5c;
    --shadow: rgba(0, 0, 0, 0.18);
  }
  * { margin: 0; padding: 0; box-sizing: border-box; }
  html, body { width: 1200px; height: 664px; overflow: hidden; }
  body {
    background: var(--bg);
    font-family: "Exo 2", Arial, sans-serif;
    position: relative;
  }
  .card {
    position: absolute;
    top: 182px;
    width: 520px;
    height: 300px;
    box-shadow: 0 6px 18px var(--shadow);
    overflow: hidden;
  }
  .card--front { left: 50px; background: var(--card-white); }
  .card--back { left: 630px; background: var(--brand-blue); }
  .card__swoosh { position: absolute; inset: 0; width: 520px; height: 300px; }

  .brand {
    position: absolute;
    left: 150px;
    top: 34px;
    display: flex;
    align-items: center;
    gap: 10px;
  }
  .brand__dot {
    width: 28px; height: 28px; border-radius: 50%;
    background: var(--logo-grey);
  }
  .brand__name {
    font-size: 28px;
    font-weight: 400;
    color: var(--logo-grey);
    letter-spacing: 0.5px;
    white-space: nowrap;
  }
  .slogan {
    position: absolute;
    left: 188px;
    top: 76px;
    font-size: 13.5px;
    color: var(--ink);
    white-space: nowrap;
  }
  .person { position: absolute; left: 120px; top: 150px; text-align: right; }
  .person__name { font-size: 21px; color: var(--brand-blue); }
  .person__title { font-size: 12px; color: var(--ink); margin-top: 1px; }

  .contacts {
    position: absolute;
    left: 340px;
    top: 112px;
    list-style: none;
    font-size: 14px;
    color: var(--ink);
    line-height: 20px;
  }
  .contacts li { display: flex; align-items: center; gap: 6px; }
  .contacts svg { width: 10px; height: 10px; fill: var(--brand-blue); flex: none; }
  .address {
    position: absolute;
    left: 356px;
    top: 206px;
    line-height: 20px;
    font-size: 14px;
    color: var(--ink);
  }

  .back-brand {
    position: absolute;
    left: 0; right: 0; top: 70px;
    display: flex; flex-direction: column; align-items: center; gap: 14px;
  }
  .back-brand__dot { width: 90px; height: 90px; border-radius: 50%; background: var(--card-white); }
  .back-brand__name { font-size: 24px; color: var(--card-white); letter-spacing: 0.5px; }
  .back-web {
    position: absolute;
    left: 0; right: 0; bottom: 28px;
    text-align: center;
    font-size: 17px;
    letter-spacing: 5px;
    color: var(--card-white);
  }
</style>
</head>
<body>

<section class="card card--front" aria-label="Business card front">
  <svg class="card__swoosh" viewBox="0 0 520 300" aria-hidden="true">
    <path d="M0 40 C 55 95, 80 190, 130 240 C 180 290, 270 285, 325 215 C 318 258, 300 285, 285 300 L0 300 Z" fill="var(--brand-blue)"/>
  </svg>

  <div class="brand">
    <span class="brand__dot"></span>
    <span class="brand__name">TOLVIN International</span>
  </div>
  <p class="slogan">Simple Solutions For Complex Problems</p>

  <div class="person">
    <p class="person__name">Your Name</p>
    <p class="person__title">Title</p>
  </div>

  <ul class="contacts">
    <li><svg viewBox="0 0 10 10"><path d="M2 0 L4 2.5 L3 3.8 Q4.5 6 6.2 7 L7.5 6 L10 8 L8.5 10 Q3 9 0 1.5 Z"/></svg>0123 456789</li>
    <li><svg viewBox="0 0 10 10"><rect x="2" y="0" width="6" height="10" rx="1"/></svg>0123 456789</li>
    <li><svg viewBox="0 0 10 10"><rect x="0" y="2" width="10" height="7" rx="1"/></svg>info@tolvin.com</li>
    <li><svg viewBox="0 0 10 10"><circle cx="5" cy="5" r="5"/></svg>www.tolvin.com</li>
  </ul>
  <p class="address">00, Complex name<br>City, State 0042</p>
</section>

<section class="card card--back" aria-label="Business card back">
  <div class="back-brand">
    <span class="back-brand__dot"></span>
    <span class="back-brand__name">TOLVIN International</span>
  </div>
  <p class="back-web">www.tolvin.com</p>
</section>

</body>
</html>
```